Harborline Hire Business Card Design

Need business cards designed for our new equipment rental. We specialize in renting to landscape / tree professionals, contractors, Do-It-Yourself'ers and Around the home or office. Looking for a eye catching card. Landscape and construction should be the theme. The logo is attached, and you can see our colors from the logo. You can use whatever color goes with it ok.

Target Market(s)

First off Landscape and Tree Professional. Then contractors, Do-It-Yourself'ers and rentals for Around the home or office.

Industry/Entity Type

Business

Contact Information for Business Card

Eye catching background that blends landscaping with construction equipment

Requirements
Must have
• Name on Card will Be: Martin Kolbeck (Manager)
• My Direct Phone Number is: 352-817-3062
• martin@harborlinehire.com
• www.harborlinehire.com
• 4712 Willow Brook Lane,
• Dade City FL 33590
Nice to have
• Would be Nice to have these bullets on the Face of the card that does not have all my information.
• Serving:
• Landscape / Tree Professionals
• Contractors
• DYI'ers or say Do-It-Yourself'ers
• Maybe have serving small and centered above these bullets, and these 3 bullets along the bottom of the card. Ideas?

```html
<!DOCTYPE html>
<html lang="en">
<head>
<meta charset="utf-8">
<title>Harborline Hire Business Card Design</title>
<link href="https://fonts.googleapis.com/css2?family=PT+Sans:wght@400;700&display=swap" rel="stylesheet">
<style>
  :root {
    --stage: #9a9a9a;
    --card-white: #ffffff;
    --navy: #0c3d6a;
    --navy-back: #0b4170;
    --navy-faint: #15507f;
    --slate: #8c8f93;
    --ink: #1d1d1f;
    --rule: #b9b9b9;
    --paper-white: #ffffff;
  }
  * { box-sizing: border-box; margin: 0; padding: 0; }
  html, body {
    width: 1200px; height: 900px; overflow: hidden;
    background: var(--stage);
    font-family: "PT Sans", Arial, sans-serif;
  }
  .stage { position: relative; width: 1200px; height: 900px; }

  .card {
    position: absolute; top: 306px; width: 439px; height: 271px;
    border-radius: 12px;
    box-shadow: 3px 4px 6px rgba(0,0,0,0.45);
    overflow: hidden;
  }
  .card--front { left: 149px; background: var(--card-white); }
  .card--back { left: 609px; background: var(--navy-back); }

  .brand-mark {
    position: absolute; left: 20px; top: 142px; width: 220px;
    text-align: center;
    font-weight: 700; font-size: 25px; letter-spacing: 0.5px;
    color: var(--navy); line-height: 1.1;
  }
  .divider {
    position: absolute; left: 247px; top: 62px; width: 1px; height: 144px;
    background: var(--rule);
  }
  .details { position: absolute; left: 260px; top: 58px; color: var(--ink); }
  .person-name {
    font-size: 15px; font-weight: 700; letter-spacing: 0.5px; color: var(--navy);
    line-height: 18px;
  }
  .person-name .surname { color: var(--slate); }
  .person-role { font-size: 12.5px; line-height: 16px; margin-bottom: 5px; }
  .contact-list { list-style: none; }
  .contact-list li {
    display: flex; align-items: center; gap: 6px;
    font-size: 12.5px; line-height: 16px;
  }
  .contact-list svg { width: 9px; height: 9px; flex: none; fill: var(--navy); }
  .address { font-size: 12.5px; line-height: 16px; margin-top: 3px; }

  .back-texture {
    position: absolute; inset: 0;
    background: linear-gradient(135deg, var(--navy-faint), var(--navy-back) 60%);
  }
  .back-brand {
    position: absolute; left: 0; right: 0; top: 140px;
    text-align: center; font-weight: 700; font-size: 12px;
    color: var(--paper-white); letter-spacing: 0.4px;
  }
</style>
</head>
<body>
<main class="stage">
  <section class="card card--front" aria-label="Business card front">
    <div class="brand-mark">HARBORLINE HIRE</div>
    <div class="divider"></div>
    <div class="details">
      <p class="person-name">MARTIN <span class="surname">KOLBECK</span></p>
      <p class="person-role">Manager</p>
      <ul class="contact-list">
        <li><svg viewBox="0 0 10 10" aria-hidden="true"><path d="M1 4c0-2 2-3 4-3s4 1 4 3H7V3H3v1z M2 5h6l1 4H1z"/></svg>352-817-3062</li>
        <li><svg viewBox="0 0 10 10" aria-hidden="true"><path d="M3 0h4a1 1 0 0 1 1 1v8a1 1 0 0 1-1 1H3a1 1 0 0 1-1-1V1a1 1 0 0 1 1-1zm0 1.5v6h4v-6z"/></svg>352-817-3062</li>
        <li><svg viewBox="0 0 10 10" aria-hidden="true"><path d="M3 0h4v3H3z M1 4h8v6H1z"/></svg>352-817-3062</li>
        <li><svg viewBox="0 0 10 10" aria-hidden="true"><path d="M0 2h10v6H0z"/><path d="M0 2l5 3.5L10 2" stroke="#fff" stroke-width="1" fill="none"/></svg>martin@harborlinehire.com</li>
        <li><svg viewBox="0 0 10 10" aria-hidden="true"><circle cx="5" cy="5" r="5"/><path d="M0 5h10M5 0c-2 3-2 7 0 10M5 0c2 3 2 7 0 10" stroke="#fff" stroke-width="0.8" fill="none"/></svg>www.harborlinehire.com</li>
      </ul>
      <p class="address">4712 Willow Brook Lane,<br>Dade City FL 33590</p>
    </div>
  </section>

  <section class="card card--back" aria-label="Business card back">
    <div class="back-texture" role="img" aria-label="Faint repeated brand pattern on navy"></div>
    <div class="back-brand">HARBORLINE HIRE</div>
  </section>
</main>
</body>
</html>
```